Mandarin tuition, language and travel services

We need a website for a new startup company, which offers Mandarin tuition, translating and interpreting, and travel services. Our company is based in Jersey, a British channel island. We would like a creative and modern professional website. Preferably with some animations. The attached is a website, which style we would prefer:
http://www.quorvabelt.net/
We have also attached our logo for your reference
We would also like to see designs using black, red and orange, which corresponds with our logo colours. The cartoon images could be travel resorts in China, and the president of China waving to the web-browsers. Of course, we wouldn't wish to restrain the designers creativity. Any creative and interesting ideas are welcomed! We look forward to hearing from you!

Target Market(s)

school children and adults

Industry/Entity Type

It Company

Number of Pages Required

3 page

Requirements
Must have
• We would prefer a small 3 pages website, if possible. The 3 pages need to be Services, News Room, and Contact us.

```html
<!DOCTYPE html>
<html lang="en">
<head>
<meta charset="utf-8">
<title>Mingyu Studio – Mandarin Tuition, Translating &amp; Travel</title>
<link rel="stylesheet" href="https://fonts.googleapis.com/css2?family=Alfa+Slab+One&family=Arvo:wght@700&family=Open+Sans:wght@400;700&display=swap">
<style>
:root{
  --red:#d90f0f;
  --black:#111111;
  --header:#1c1c1c;
  --ink:#222222;
  --text:#333333;
  --muted:#555555;
  --panel:#efefef;
  --line:#d6d6d6;
  --white:#ffffff;
}
*{box-sizing:border-box;margin:0;padding:0}
html,body{width:872px;height:1200px;overflow:hidden;background:var(--white)}
body{position:relative;font-family:"Open Sans",Arial,sans-serif;color:var(--text)}
.abs{position:absolute}

/* header */
.site-header{left:0;top:0;width:872px;height:62px;background:repeating-linear-gradient(45deg,#222 0 2px,#161616 2px 4px);border-bottom:2px solid var(--red)}
.brand-disc{left:72px;top:-32px;width:124px;height:130px;border-radius:50%;background:var(--white);display:flex;align-items:flex-end;justify-content:center;padding-bottom:36px;z-index:3}
.brand-name{font-family:"Alfa Slab One",Georgia,serif;font-size:15px;line-height:1.05;color:var(--black);text-align:center}
.main-nav{right:72px;top:0;height:62px;display:flex;align-items:center;z-index:2}
.main-nav a{font-family:"Arvo",Georgia,serif;font-weight:700;font-size:12px;color:var(--white);text-decoration:none;padding:0 27px;border-left:1px solid #555;line-height:12px}
.main-nav a:first-child{border-left:none}
.main-nav a:last-child{padding-right:0}

/* hero */
.hero{left:0;top:62px;width:872px;height:376px;background:linear-gradient(180deg,#14203f 0%,#24365e 35%,#5a4630 62%,#2c4f6a 78%,#3f8cb5 100%)}
.hero-band{left:0;top:264px;width:470px;height:91px;background:rgba(20,20,20,.78);clip-path:polygon(0 0,440px 0,470px 100%,0 100%)}
.hero-title{left:73px;top:280px;font-family:"Arvo",Georgia,serif;font-weight:700;font-size:19.5px;line-height:27px;color:var(--white)}

/* about + news */
.intro-band{left:0;top:438px;width:872px;height:245px;background:var(--panel)}
.section-title{font-family:"Alfa Slab One",Georgia,serif;font-size:24px;font-weight:400;color:var(--black);display:flex;align-items:center;gap:6px;white-space:nowrap}
.section-title em{font-style:normal;color:var(--red)}
.title-dot{width:20px;height:20px;border-radius:50%;background:var(--red);margin-top:-18px}
.about-title{left:73px;top:462px}
.about-copy{left:73px;top:499px;width:344px;font-size:10.6px;line-height:18px;color:var(--text);text-align:justify}
.read-more{left:72px;top:623px;width:88px;height:28px;background:var(--red);color:var(--white);font-size:10.5px;font-weight:700;display:flex;align-items:center;justify-content:center;border-radius:2px}
.divider{left:435px;top:470px;width:1px;height:175px;background:var(--line)}
.news-title{left:462px;top:462px}
.news-item{left:462px;width:340px;height:62px;display:flex;gap:13px}
.news-thumb{width:94px;height:62px;border:1px solid #777;padding:3px;background:var(--white)}
.news-thumb div{width:100%;height:100%}
.news-body{font-size:9.3px;line-height:14px;color:var(--muted);width:232px}
.news-date{color:var(--red);font-weight:700;font-size:9.8px;margin-bottom:5px;display:block}
.news-body b{color:#333}
.more{color:var(--red);font-weight:700}
.news-sep{left:462px;top:578px;width:340px;height:1px;background:var(--line)}

/* services */
.services-title{left:0;top:700px;width:872px;justify-content:center;font-size:24px}
.services-lead{left:136px;top:746px;width:600px;text-align:center;font-size:9px;line-height:14.5px;color:var(--text)}
.service-card{top:786px;width:230px;height:311px;border:1px solid var(--line);background:var(--white);overflow:hidden}
.service-photo{position:absolute;left:0;width:100%;height:183px}
.service-info{position:absolute;left:0;width:100%;text-align:center}
.service-name{font-family:"Arvo",Georgia,serif;font-weight:700;font-size:15px;color:#2a2a2a}
.service-rule{width:98px;height:1px;background:#444;margin:8px auto 14px;position:relative}
.service-rule::after{content:"";position:absolute;left:39px;top:-1px;width:20px;height:3px;background:var(--red)}
.service-text{font-size:10.2px;line-height:16px;color:#444;padding:0 14px}
.service-text b{color:#222}

/* footer */
.contact-bar{left:0;top:1129px;width:872px;height:41px;background:var(--black);display:flex;align-items:center;padding:0 72px;color:#e6e6e6;font-size:10.5px}
.contact-item{display:flex;align-items:center;gap:7px;margin-right:16px}
.contact-phone{font-size:13px}
.social{margin-left:auto;display:flex;gap:5px}
.social span{width:20px;height:20px;border-radius:50%;background:var(--white)}
.copyright{left:0;top:1170px;width:872px;height:30px;background:var(--red);color:var(--white);font-size:9.6px;font-weight:700;display:flex;align-items:center;justify-content:center}
</style>
</head>
<body>

<header>
  <div class="abs site-header"></div>
  <div class="abs brand-disc"><span class="brand-name">Mingyu<br>Studio</span></div>
  <nav class="abs main-nav">
    <a href="#">Home</a>
    <a href="#">Our Services</a>
    <a href="#">News Room</a>
    <a href="#">Contact Us</a>
  </nav>
</header>

<section>
  <div class="abs hero" role="img" aria-label="Evening view of a resort hotel with tiered roofs, palm trees and a lit pool"></div>
  <div class="abs hero-band"></div>
  <h1 class="abs hero-title">Full Immersion Foreign Language<br>Courses For school children and adults.</h1>
</section>

<section>
  <div class="abs intro-band"></div>

  <h2 class="abs section-title about-title">About <em>Mingyu Studio</em><span class="title-dot"></span></h2>
  <p class="abs about-copy">Lorem Ipsum is simply dummy text of the printing and typesetting industry. Lorem Ipsum has been the industry's standard dummy text ever since the 1500s, when an unknown printer took a galley of type and scrambled it to make a type specimen book. It has survived not only five centuries, but also the leap into electronic typesetting, remaining essentially unchanged.</p>
  <div class="abs read-more">Read More</div>

  <div class="abs divider"></div>

  <h2 class="abs section-title news-title">News <em>Room</em><span class="title-dot"></span></h2>
  <article class="abs news-item" style="top:503px">
    <div class="news-thumb"><div role="img" aria-label="Two people in a meeting at a table" style="background:linear-gradient(135deg,#5c3e2a,#b89a78)"></div></div>
    <p class="news-body"><span class="news-date">04 Dec, 2015</span><b>Duis autem vel eum iriure dolor</b> in hendrerit ink bol vulputate velit esse molestie consequat, velmil noi illum dolore eu feugiat nulla facilisis... <span class="more">[+]</span></p>
  </article>
  <div class="abs news-sep"></div>
  <article class="abs news-item" style="top:590px">
    <div class="news-thumb"><div role="img" aria-label="Businesswoman at a desk shaking hands" style="background:linear-gradient(135deg,#3c3c3c,#8a8f7a)"></div></div>
    <p class="news-body"><span class="news-date">04 Dec, 2015</span><b>Duis autem vel eum iriure dolor</b> in hendrerit ink bol vulputate velit esse molestie consequat, velmil noi illum dolore eu feugiat nulla facilisis... <span class="more">[+]</span></p>
  </article>
</section>

<section>
  <h2 class="abs section-title services-title">Our&nbsp;<em>Service</em><span class="title-dot"></span></h2>
  <p class="abs services-lead">Lorem Ipsum is simply dummy text of the printing and typesetting industry. Lorem Ipsum has been the industry's standard dummy text ever since the 1500s, when it to make a type specimen book.</p>

  <article class="abs service-card" style="left:72px">
    <div class="service-photo" style="top:0;background:linear-gradient(135deg,#3a302a,#c9b8a4 60%,#e8ddd0)" role="img" aria-label="Teacher guiding students with calligraphy brushes"></div>
    <div class="service-info" style="top:212px">
      <h3 class="service-name">Mandarin Tuition</h3>
      <div class="service-rule"></div>
      <p class="service-text">Lorem ipsum dolor sit amet, consectetuer adipiscing elit... <b>[ + ]</b></p>
    </div>
  </article>

  <article class="abs service-card" style="left:321px">
    <div class="service-info" style="top:28px">
      <h3 class="service-name">Translating &amp; Interpreting</h3>
      <div class="service-rule"></div>
      <p class="service-text">Lorem ipsum dolor sit amet, consectetuer adipiscing elit... <b>[ + ]</b></p>
    </div>
    <div class="service-photo" style="top:127px;height:184px;background:linear-gradient(90deg,#8c95a8,#6a5a4a 55%,#b4762e)" role="img" aria-label="Two interpreters working in a booth with microphones"></div>
  </article>

  <article class="abs service-card" style="left:570px">
    <div class="service-photo" style="top:0;background:linear-gradient(135deg,#9a8a70,#d8c7b0 45%,#6b8ab0)" role="img" aria-label="Travel agent helping a boy at a booking desk"></div>
    <div class="service-info" style="top:212px">
      <h3 class="service-name">Travel Services</h3>
      <div class="service-rule"></div>
      <p class="service-text">Lorem ipsum dolor sit amet, consectetuer adipiscing elit... <b>[ + ]</b></p>
    </div>
  </article>
</section>

<footer>
  <div class="abs contact-bar">
    <span class="contact-item">
      <svg width="14" height="18" viewBox="0 0 14 18" aria-hidden="true"><path d="M7 0a7 7 0 0 0-7 7c0 5 7 11 7 11s7-6 7-11a7 7 0 0 0-7-7z" fill="#ddd"/><circle cx="7" cy="7" r="2.6" fill="#111"/></svg>
      Lorem ipsum dolor sit amet, adipiscing elit
    </span>
    <span class="contact-item contact-phone">
      <svg width="12" height="16" viewBox="0 0 12 16" aria-hidden="true"><path d="M3 0l3 4-2 2c1 2 2 4 4 5l2-2 3 3-2 3C5 15 0 8 1 2z" fill="#ddd"/></svg>
      123-456-7890
    </span>
    <span class="contact-item">
      <svg width="16" height="12" viewBox="0 0 16 12" aria-hidden="true"><rect width="16" height="12" rx="1" fill="#ddd"/><path d="M0 1l8 6 8-6" stroke="#111" stroke-width="1.4" fill="none"/></svg>
      hello@mingyustudio.com
    </span>
    <div class="social" aria-label="Social links"><span></span><span></span><span></span><span></span></div>
  </div>
  <div class="abs copyright">Copyright 2016 Mingyu Studio. All rights reserved.</div>
</footer>

</body>
</html>
```